TRNV LLP website - revamping our website after 23 years

Our website needs a complete overhaul. The purpose of this exercise is to provide us with your vision of what you think the website should look like. We don't need the website to be created or coded. Just need creative designs.

We have a four sites that we would like to base our website on;

We like the simplicity of Fairwicks, the style of Pemberly Strand and Kettridge.

http://www.pemberlystrand-example.com/en/toronto-ontario/
http://www.fairwicks-example.ca/
hallkettridge-example.com
http://www.vendrupe-example.com/our-professionals.html

We have a logo that we would like to use which will be attached below. We need to keep our website looking very professional as we have a large number of high net worth clients.
Updates

Hi, We've received some good website designs but they appear to be the same type of template websites we've received in the past - this is not what we're looking for. What we want is a unique website that is modelled on the following three company websites: http://www.fairwicks-example.ca/ www.hallkettridge-example.com/ http://www.pemberlystrand-example.com/en/toronto-ontario/

Thank you everyone for your designs. I will be posting updates and my comments on the various designs in the next day - I want to thank you for the creative designs I see. I thought i would explain a bit about our firm and perhaps it can help when you design the theme of our website: - Our firm is like a family and our clients are truly like our friends. We have close knit relationships in and outside of the office with staff and clients. - We are an 'out of the box' type of firm. We operate differently than most firms and that's a differentiating factor in what makes us who we are - Our slogan is "Count on us" which is a testament to the way we run our practice - We would like an open, fresh, clean look to our website - we don't want the landing page to be overly long or complex because we have limited time to update the website and limited content That's it for the time being - when things come to mind I will post them here.

Can we try a design as follows: - make the website look very similar to www.fairwicks-example.ca - use the same background colour - Keep the same black top but insert our logo - incorporate some of the content from our current website www.trnv-example.com

I have been away dealing with a personal matter. I will look into these websites tomorrow afternoon and provide more feedback / info on the top designer. Thank you

Hi designers, I want to apologize for the delay. I plan on wrapping things up within the next few days. I will go through a few of the top designs and offer my comments. Thank you for your patience.

Target Market(s)

Mainly our current clients - We have a large number of high net worth individuals as clients.

Industry/Entity Type

Accounting

Number of Pages Required

1 page

Requirements
Must have
• Please model website on the websites indicated above.
• Our current website is www.trnv-example.com. It's dark, cluttered and not inviting. We want a fresh, clean website. Please incorporate the logo's attached below.

```html
<!DOCTYPE html>
<html lang="en">
<head>
<meta charset="utf-8">
<title>TRNV LLP — Chartered Professional Accountants</title>
<link rel="stylesheet" href="https://fonts.googleapis.com/css2?family=Vollkorn:ital,wght@0,400;0,600;0,700;1,700&family=Source+Sans+3:wght@400;600&display=swap">
<style>
:root{
  --ink:#111;
  --black:#000;
  --header-top:#2a2a2a;
  --header-bottom:#050505;
  --muted:#8a8a8a;
  --white:#fff;
  --lime:#8cc63f;
  --magenta:#a3195b;
  --hero-bg:#f3f3f3;
  --band:rgba(170,194,207,.78);
  --rule:rgba(255,255,255,.5);
  --footer-link:#7d7d7d;
}
*{box-sizing:border-box;margin:0;padding:0}
html,body{width:1200px;height:960px;overflow:hidden;background:var(--white)}
body{font-family:"Source Sans 3",Arial,sans-serif;color:var(--ink);position:relative;font-variant-numeric:lining-nums}

.info-bar{position:absolute;top:7px;left:0;width:1200px;height:36px;background:var(--black);
  font-family:"Vollkorn",Georgia,serif;font-size:14px;color:var(--muted);display:flex;align-items:center;padding-left:73px;gap:18px}
.info-bar .item{display:flex;align-items:center;gap:6px}
.info-bar b{color:var(--white);font-weight:600}
.info-bar svg{fill:none;stroke:var(--white);stroke-width:1.6}

.site-header{position:absolute;top:43px;left:0;width:1200px;height:113px;
  background:linear-gradient(var(--header-top),var(--header-bottom) 70%)}
.brand{position:absolute;left:73px;top:14px;display:flex;align-items:center;gap:14px}
.brand .mark{width:72px;height:72px;border:3px solid var(--white)}
.brand .name{font-family:"Vollkorn",Georgia,serif;font-size:42px;color:var(--white);letter-spacing:1px}
.slogan{position:absolute;left:442px;top:46px;font-family:"Vollkorn",Georgia,serif;font-size:22px;color:var(--lime)}
.slogan-rule{position:absolute;left:560px;top:73px;width:565px;height:1px;background:#2c2c2c}

.hero{position:absolute;top:156px;left:60px;width:1080px;height:444px;background:var(--hero-bg);overflow:hidden}
.hero-photo{position:absolute;right:0;top:0;width:640px;height:444px;
  background:radial-gradient(ellipse at 70% 40%,#3d4c66 0%,#6b7b92 35%,#b7c1cc 60%,rgba(243,243,243,0) 80%),
  linear-gradient(90deg,rgba(243,243,243,1) 0%,rgba(210,216,224,.6) 40%,#c4ccd6 100%)}
.main-nav{position:absolute;top:185px;left:73px;display:flex;align-items:center;
  font-family:"Vollkorn",Georgia,serif;font-size:15px;color:#333;text-transform:uppercase}
.main-nav a{color:inherit;text-decoration:none;margin-right:38px}
.main-nav svg{margin-right:14px;fill:#333}
.search{position:absolute;top:183px;left:1051px;display:flex;align-items:center;gap:10px;color:var(--white);font-size:16px}
.search svg{fill:none;stroke:var(--white);stroke-width:2.4}

.hero-copy{position:absolute;left:73px;top:350px;font-family:"Vollkorn",Georgia,serif;color:var(--ink);font-size:21px;line-height:30px}
.hero-copy strong{font-size:31px;font-weight:700}
.hero-copy .num{font-size:38px;font-style:italic;font-weight:700;color:var(--magenta);margin-left:10px}
.hero-copy .years{color:var(--magenta);font-weight:600}

.feature-band{position:absolute;top:600px;left:60px;width:1080px;height:183px;background:var(--band)}
.feature{position:absolute;top:14px;width:250px}
.feature h2{font-family:"Vollkorn",Georgia,serif;font-size:22px;font-weight:600;color:var(--ink);white-space:nowrap}
.feature h3{font-family:"Vollkorn",Georgia,serif;font-size:16px;font-weight:400;margin-top:2px;padding-bottom:12px;border-bottom:1px solid var(--rule);white-space:nowrap}
.feature p{font-size:15px;line-height:22px;margin-top:12px;width:240px}
.feature .more-link{position:absolute;top:144px;font-size:13px;color:var(--ink)}
.more-btn{position:absolute;left:974px;top:66px;width:34px;text-align:center;color:var(--white);font-size:12px}

.site-footer{position:absolute;top:818px;left:0;width:1200px}
.foot-col{position:absolute;top:0}
.foot-col h4{font-family:"Vollkorn",Georgia,serif;font-size:15px;font-weight:400;color:#333;text-transform:uppercase;margin-bottom:9px}
.foot-col li{list-style:none;font-size:13px;color:var(--footer-link);line-height:18.5px}
</style>
</head>
<body>

<div class="info-bar">
  <span class="item"><svg width="13" height="13" viewBox="0 0 14 14"><circle cx="7" cy="7" r="5.8"/><path d="M7 3.5V7l2.2 1.6"/></svg>Hours of Operation : <b>9:00am to 5:00pm</b></span>
  <span class="item"><svg width="15" height="14" viewBox="0 0 16 16"><path d="M3 2l3 .5 1 3-1.6 1.2a8 8 0 0 0 3.9 3.9L10.5 9l3 1 .5 3c-6 1-12-5-11-11z"/></svg>Call Us : <b>(416) 555-0148</b></span>
  <span class="item"><svg width="15" height="11" viewBox="0 0 16 12"><rect x="1" y="1" width="14" height="10"/><path d="M1 1l7 6 7-6"/></svg>Email Us : <b>info@trnv-example.com</b></span>
</div>

<header class="site-header">
  <div class="brand"><span class="mark"></span><span class="name">TRNV LLP</span></div>
  <div class="slogan">Count on us !</div>
  <div class="slogan-rule"></div>
</header>

<section class="hero">
  <div class="hero-photo" role="img" aria-label="Photograph of two accountants in suits reviewing documents at a desk"></div>
</section>

<nav class="main-nav">
  <svg width="16" height="14" viewBox="0 0 16 14"><path d="M8 0l8 7h-2v7h-4V9H6v5H2V7H0z"/></svg>
  <a href="#">About&nbsp; TRNV</a><a href="#">Services</a><a href="#">Library</a><a href="#">Links</a><a href="#">Careers</a><a href="#">Contact Us</a>
</nav>
<div class="search">Search <svg width="17" height="17" viewBox="0 0 18 18"><circle cx="7.5" cy="7.5" r="5.5"/><path d="M11.5 11.5l5 5"/></svg></div>

<div class="hero-copy">
  <div><strong>Together</strong>, We bring over <span class="num">100</span> <span class="years">Years</span> of</div>
  <div>Valuable Experience to the pratice of public accounting</div>
</div>

<section class="feature-band">
  <article class="feature" style="left:32px">
    <h2>2015 Tax Estimator</h2><h3>For 2014 Now Online!</h3>
    <p>Lorem ipsum dolor sit amet, aliquam erat volutpat. Ut wisi enim ...</p>
    <span class="more-link">[READ MORE]</span>
  </article>
  <article class="feature" style="left:301px">
    <h2>TRNV Tax Tips</h2><h3>Tax Exemption For Scholarships!</h3>
    <p>Lorem ipsum dolor sit amet, aliquam erat volutpat. Ut wisi enim ...</p>
    <span class="more-link">[READ MORE]</span>
  </article>
  <article class="feature" style="left:571px">
    <h2>Why We Are Different</h2><h3>For 2014 Now Online!</h3>
    <p>Lorem ipsum dolor sit amet, aliquam erat volutpat. Ut wisi enim ...</p>
    <span class="more-link">[READ MORE]</span>
  </article>
  <div class="more-btn">
    <svg width="32" height="14" viewBox="0 0 32 14"><path d="M2 13V7L16 1l14 6v6L16 7z" fill="#fff"/></svg>
    <div>MORE</div>
    <svg width="32" height="14" viewBox="0 0 32 14"><path d="M2 1v6l14 6 14-6V1L16 7z" fill="#fff"/></svg>
  </div>
</section>

<footer class="site-footer">
  <div class="foot-col" style="left:73px"><h4>Contact Us</h4><ul><li>Feedback</li><li>Directions</li><li>Hours of Operation</li><li>Contact an&nbsp; Individual</li></ul></div>
  <div class="foot-col" style="left:253px"><h4>About Us</h4><ul><li>Who We Are</li><li>Why We Are Different</li><li>Partner Information</li><li>Staff Profiles</li></ul></div>
  <div class="foot-col" style="left:434px"><h4>Careers</h4><ul><li>Career Opportunities at&nbsp; TRNV</li><li>E-Mail Us</li></ul></div>
  <div class="foot-col" style="left:645px"><h4>&nbsp;Login</h4><ul><li>@TRNV LLP</li><li>All Rights Reserved</li></ul></div>
</footer>

</body>
</html>
```